Veloura Cosmetic Clinic Brochure

I require a high end, luxurious yet natural brochure for my Lumitox clinic. I prefer the colours blue and silver with white. I was unable to upload the professional images of my clinic but would forward these 9the images were too big).

Target Market(s)

40 to 50 year olds

Industry/Entity Type

Lumitox and cosmetic treatments

Colors
0054AA
0677BA
7BADD7
CADEEF
E8F1F8

Requirements
Nice to have
• blue and silver colours

```html
<!DOCTYPE html>
<html lang="en">
<head>
<meta charset="utf-8">
<title>Veloura Cosmetic Clinic Brochure</title>
<link href="https://fonts.googleapis.com/css2?family=Cinzel:wght@400;600;700&family=Lato:wght@400;700&display=swap" rel="stylesheet">
<style>
:root{
  --navy:#0054AA;--blue:#0677BA;--sky:#7BADD7;--mist:#CADEEF;--ice:#E8F1F8;
  --silver:#c5c9cf;--silver-dark:#9aa0a8;--ink:#2a2a2a;--page:#e6e9ed;
}
*{margin:0;padding:0;box-sizing:border-box}
html,body{width:902px;height:1200px;overflow:hidden;background:var(--page)}
body{font-family:'Lato',sans-serif;color:var(--ink);position:relative}
.spread{position:absolute;left:41px;width:820px;height:583px;background:#fff;box-shadow:0 4px 14px rgba(0,0,0,.25);overflow:hidden}
.spread--outside{top:10px}
.spread--inside{top:607px}
.panel{position:absolute;top:0;width:273.33px;height:583px;overflow:hidden}
.panel--1{left:0}.panel--2{left:273.33px}.panel--3{left:546.66px}
.abs{position:absolute}
.bg-svg{position:absolute;inset:0;width:100%;height:100%}
.serif{font-family:'Cinzel',serif}
.body-text{font-size:8.4px;line-height:1.28;text-align:justify}
.body-text p{margin-bottom:7px}
.pill{position:absolute;left:50%;transform:translateX(-50%);white-space:nowrap;font-family:'Cinzel',serif;font-weight:700;font-size:11.5px;letter-spacing:.5px;padding:3px 16px;border-radius:12px;border:1.5px solid #e3e6ea;box-shadow:0 1px 3px rgba(0,0,0,.3)}
.pill--blue{background:linear-gradient(#4fa5e6,var(--blue) 55%,var(--navy));color:#fff}
.pill--silver{background:linear-gradient(#fff,#e4e6e9 60%,#c8ccd1);color:#2a2a2a}
.footer-band{position:absolute;left:0;right:0;bottom:0;height:32px;background:linear-gradient(#f4f5f6,#c9cdd2);display:flex;align-items:center;justify-content:center;gap:5px;font-size:12px;font-weight:700;color:#222}
.globe{width:9px;height:9px}
.photo{position:absolute}
.brand{display:flex;align-items:center;gap:6px;font-family:'Lato',sans-serif;font-weight:400;color:var(--blue)}
.brand__dot{border-radius:50%;background:var(--blue)}
.brand__name{letter-spacing:2px}
.white{color:#fff}
.center{text-align:center}
.link{font-size:8.4px;text-decoration:underline;color:#222}
.tab{position:absolute;font-family:'Cinzel',serif;font-weight:700;font-size:9px;letter-spacing:.4px;padding:2px 8px;border-radius:9px;white-space:nowrap}
.tab--blue{background:linear-gradient(var(--blue),var(--navy));color:#fff;border:1px solid #dfe3e8}
.tab--grey{background:linear-gradient(#eef0f2,#b9bec5);color:#222}
.rule{position:absolute;height:1.5px;background:var(--navy)}
.days{font-size:8px;line-height:1.35;font-weight:700;color:#fff}
.contact-line{display:flex;align-items:center;justify-content:center;gap:5px;color:#fff;font-weight:700}
.social{display:flex;align-items:center;gap:5px;color:#fff;font-size:7px;font-weight:700}
.social__mark{width:7px;height:7px;background:#fff;border-radius:1px}
.bottom-band{position:absolute;left:0;right:0;bottom:0;height:24px;background:linear-gradient(90deg,var(--navy),var(--blue))}
</style>
</head>
<body>

<section class="spread spread--outside">

  <div class="panel panel--1" style="background:linear-gradient(90deg,#fff 70%,#e9eaec)">
    <svg class="bg-svg" viewBox="0 0 273 583" preserveAspectRatio="none" aria-hidden="true">
      <path d="M0 0H273V30C200 20 90 35 0 80Z" fill="#5bb0ea"/>
      <path d="M0 80C90 35 200 20 273 30V42C190 34 90 50 0 92Z" fill="#d2d6db"/>
    </svg>
    <div class="pill pill--blue" style="top:90px">Introduction</div>
    <div class="abs body-text" style="left:22px;top:122px;width:230px">
      <p>VELOURA is a doctor led medical cosmetic clinic founded by Dr Elena Marsh.</p>
      <p>We provide state of the art, innovative and natural cosmetic treatments in combination with lifestyle advice based on your genetic make up. This unique combination provides you with a holistic approach to your health, wellbeing and overall appearance.</p>
      <p>Our beautiful clinic is situated in a hidden yet easily accessible location, so that you can have absolute privacy. We pride ourselves in providing a relaxed, comfortable athmosphere in a down to earth setting.</p>
      <p>All treatments are performed by doctors with a meticulous approach to natural results, and we place high emphasis on confidentiality and privacy.</p>
      <p>Dr Elena Marsh is an experienced cosmetic doctor and accredited GeneWell provider who holds the Australasian Professional Diploma in Aesthetic Medicine. She is also a member of the Allied Aesthetic Society.</p>
      <p>Our most commonly requested treatments are anti wrinkle injections, Dermal Filler, PRP Plasma Facials, PRP Plasma for male baldness and GeneWell assessments.</p>
      <p>Our reputation is very important to us, and integrity is a cornerstone of our clinic in terms of the advice we offer, the treatments we provide and the standard of treatment and care that we give.</p>
      <p>We recognise that everybody is unique and treat each patient as an individual. Your ongoing well-being is our priority, with a commitment to ensure the highest standards of service and clinical care.</p>
      <p style="text-align:left;margin-top:12px">Dr Elena Marsh MRCPCH MD<br>Aesthetic Medicine Doctor</p>
    </div>
    <div class="footer-band"><svg class="globe" viewBox="0 0 10 10"><circle cx="5" cy="5" r="4.5" fill="#222"/><path d="M.5 5h9M5 .5v9M2 2.5c2 1 4 1 6 0M2 7.5c2-1 4-1 6 0" stroke="#fff" stroke-width=".7" fill="none"/></svg>www.veloura.co.nz</div>
  </div>

  <div class="panel panel--2" style="background:linear-gradient(160deg,var(--blue),var(--navy) 70%,#0a4a93)">
    <div class="pill pill--silver" style="top:105px">Contact Us</div>
    <div class="abs" style="left:0;right:0;top:136px">
      <div class="contact-line" style="font-size:14px"><svg width="11" height="11" viewBox="0 0 12 12"><circle cx="6" cy="6" r="5.3" fill="none" stroke="#fff" stroke-width="1.2"/><path d="M4 3.2l1 1.6-.6.7c.4.8 1 1.4 1.8 1.8l.7-.6 1.6 1-.5 1.2C6 8.8 3.2 6 3 4z" fill="#fff"/></svg>0800-555-019</div>
      <div class="contact-line" style="font-size:9px;margin-top:6px"><svg width="9" height="7" viewBox="0 0 9 7"><rect width="9" height="7" fill="#fff"/><path d="M0 0l4.5 3.5L9 0" stroke="#0677BA" fill="none"/></svg>enquiries@veloura.co.nz</div>
      <div class="contact-line" style="font-size:9px;margin-top:5px;align-items:flex-start"><svg width="8" height="10" viewBox="0 0 8 10"><path d="M4 0a4 4 0 0 1 4 4c0 3-4 6-4 6S0 7 0 4a4 4 0 0 1 4-4z" fill="#fff"/><circle cx="4" cy="4" r="1.5" fill="#0677BA"/></svg><span class="center">14 Harbour Lane, Kelmont,<br>Rivermouth 8041</span></div>
    </div>
    <div class="pill pill--silver" style="top:210px">Hours of Operation</div>
    <div class="abs serif white center" style="left:0;right:0;top:240px;font-size:8.6px;line-height:1.25;font-weight:600">OUR PHONES ARE NORMALLY ANSWERED<br>BETWEEN THE HOURS OF</div>
    <div class="abs days center" style="left:0;right:0;top:268px;font-size:8.4px">Monday to Friday 8.00 am to 8.00pm<br>Saturday 8.00 am to 4.00 pm</div>
    <div class="pill pill--silver" style="top:306px">Appointments</div>
    <div class="abs serif white center" style="left:0;right:0;top:340px;font-size:8.6px;font-weight:600">VELOURA COSMETIC CLINIC IS OPEN</div>
    <div class="abs days" style="left:10px;top:362px">Monday 8.00 am to 2.00 pm<br>Tuesday 8.00 am to 2.00 pm<br>Wednesday 8.00 am to 8.00 pm</div>
    <div class="abs" style="left:138px;top:362px;width:1px;height:34px;background:#9cc5ea"></div>
    <div class="abs days" style="left:146px;top:362px">Thursday 8.00 am to 8.00 pm<br>Friday 8.00 am to 2.00 pm<br>Saturday 8.00 am to 2.00 pm</div>
    <div class="photo" role="img" aria-label="Street map showing the clinic location" style="left:9px;top:408px;width:256px;height:90px;border-radius:6px;background:linear-gradient(135deg,#eef1ee,#dfe6e3)"></div>
    <div class="abs" style="left:36px;top:514px">
      <div class="social"><span class="social__mark"></span>social.example/VelouraClinic</div>
      <div class="social" style="margin-top:5px"><span class="social__mark"></span>video.example/VelouraClinic</div>
    </div>
    <div class="footer-band"><svg class="globe" viewBox="0 0 10 10"><circle cx="5" cy="5" r="4.5" fill="#222"/><path d="M.5 5h9M5 .5v9M2 2.5c2 1 4 1 6 0M2 7.5c2-1 4-1 6 0" stroke="#fff" stroke-width=".7" fill="none"/></svg>www.veloura.co.nz</div>
  </div>

  <div class="panel panel--3" style="background:#fff">
    <div class="abs brand" style="left:30px;top:38px">
      <span class="brand__dot" style="width:26px;height:26px"></span>
      <div>
        <div class="brand__name" style="font-size:28px;line-height:1">VELOURA</div>
        <div style="font-size:11px;letter-spacing:.5px">Aesthetic Doctor</div>
      </div>
    </div>
    <div class="photo" role="img" aria-label="Portrait of a smiling woman with hands framing her face" style="left:0;top:100px;width:273px;height:420px;background:radial-gradient(ellipse at 50% 45%,#f2ddd0 0,#f6ece6 35%,#fff 70%)"></div>
    <svg class="bg-svg" viewBox="0 0 273 583" preserveAspectRatio="none" aria-hidden="true">
      <path d="M0 90C80 140 200 160 273 125V103C200 140 80 125 0 70Z" fill="#0677BA"/>
      <path d="M0 100C80 150 200 170 273 135V125C200 160 80 140 0 90Z" fill="#cfd4da"/>
      <path d="M0 455C90 450 190 425 273 360V583H0Z" fill="url(#coverBlue)"/>
      <path d="M0 455C90 450 190 425 273 360V372C190 435 90 460 0 466Z" fill="#dfe3e7"/>
      <defs><linearGradient id="coverBlue" x1="0" y1="0" x2="0" y2="1"><stop offset="0" stop-color="#0677BA"/><stop offset="1" stop-color="#0054AA"/></linearGradient></defs>
    </svg>
    <div class="abs serif white center" style="left:0;right:0;top:455px;font-size:20px;line-height:1.2;letter-spacing:1px;font-weight:600">VELOURA MEDICAL<br>COSMETIC CLINIC</div>
    <div class="abs serif center" style="left:0;right:0;top:513px;font-size:11.5px;line-height:1.3;color:#0c2a4d;font-weight:600">Meticulous approach<br>to natural results</div>
    <div class="footer-band"><svg class="globe" viewBox="0 0 10 10"><circle cx="5" cy="5" r="4.5" fill="#222"/><path d="M.5 5h9M5 .5v9M2 2.5c2 1 4 1 6 0M2 7.5c2-1 4-1 6 0" stroke="#fff" stroke-width=".7" fill="none"/></svg>www.veloura.co.nz</div>
  </div>
</section>

<section class="spread spread--inside">

  <div class="panel panel--1" style="background:linear-gradient(90deg,#fff 80%,#f0f1f2)">
    <svg class="bg-svg" viewBox="0 0 273 583" preserveAspectRatio="none" aria-hidden="true">
      <path d="M214 120C240 122 258 132 273 140" stroke="#0677BA" stroke-width="2.5" fill="none"/>
    </svg>
    <div class="photo" role="img" aria-label="Clinic interior with product shelves" style="left:-14px;top:22px;width:132px;height:132px;border-radius:50%;background:linear-gradient(160deg,#d8d2c8,#a89584);border:4px solid var(--blue)"></div>
    <div class="photo" role="img" aria-label="Skincare products on display" style="left:108px;top:60px;width:104px;height:104px;border-radius:50%;background:linear-gradient(160deg,#e6e8ea,#9ea6ae);border:4px solid var(--blue)"></div>
    <div class="abs brand" style="left:130px;top:30px">
      <span class="brand__dot" style="width:16px;height:16px"></span>
      <div>
        <div class="brand__name" style="font-size:17px;line-height:1">VELOURA</div>
        <div style="font-size:7px">Aesthetic Doctor</div>
      </div>
    </div>
    <div class="pill pill--blue" style="top:218px">Treatments</div>
    <div class="abs body-text" style="left:22px;top:250px;width:236px">
      <p>During your initial consultation we will discuss your personal requirements and most appropriate treatment options. We like to take as much time as needed to find the most suitable, personalised treatment plan within a budget you feel comfortable with.</p>
      <p>It is important that you understand the pros and cons of the treatment options available, and we encourage you to ask any questions you may have.</p>
      <p>What follows is a brief overview of treatments we offer.</p>
    </div>
    <div class="rule" style="left:0;width:273px;top:393px"></div>
    <div class="tab tab--blue" style="left:18px;top:386px">Anti Wrinkle Injections</div>
    <div class="abs body-text" style="left:22px;top:412px;width:236px">
      <p>A well-established way of reducing movement-related lines in the upper face. For best results, an intimate understanding of facial anatomy combined with an individual assessment is required.</p>
      <p>The same medication can be used to treat excessive underarm sweating and treatment resistant migraine.</p>
      <p>Dr Elena offers all 3 botulinum toxin formulations that are FDA approved in New Zealand (Lumitox, Velatox and Softenin). She will discuss your personal preferences with you to find the most suitable product.</p>
      <p class="link" style="text-align:left">www.veloura.co.nz/Lumitox</p>
    </div>
    <div class="bottom-band"></div>
  </div>

  <div class="panel panel--2" style="background:#fff">
    <div class="photo" role="img" aria-label="Portrait of a smiling mature woman touching her cheek" style="left:70px;top:0;width:203px;height:215px;background:linear-gradient(160deg,#e9d8cc,#f5ede6 60%,#fff)"></div>
    <svg class="bg-svg" viewBox="0 0 273 583" preserveAspectRatio="none" aria-hidden="true">
      <path d="M0 200C90 210 200 200 273 160V583H0Z" fill="url(#innerBlue)"/>
      <path d="M0 200C90 210 200 200 273 160V170C200 212 90 220 0 210Z" fill="#dfe3e7"/>
      <defs><linearGradient id="innerBlue" x1="0" y1="0" x2="0" y2="1"><stop offset="0" stop-color="#0677BA"/><stop offset="1" stop-color="#0054AA"/></linearGradient></defs>
    </svg>
    <div class="photo" role="img" aria-label="Portrait of a smiling man" style="left:6px;top:110px;width:104px;height:104px;border-radius:50%;background:linear-gradient(160deg,#dcc6b4,#eee6de);border:4px solid var(--blue)"></div>
    <div class="tab tab--grey" style="left:12px;top:235px">Dermal Fillers</div>
    <div class="abs body-text white" style="left:14px;top:258px;width:246px">
      <p>We use dermal fillers to restore lost volume in the face to create lift and shape. But, they can also help to reduce facial lines and wrinkles and make skin appear thicker and more radiant.</p>
      <p>Veloura Cosmetic Clinic's preferred filler product is Alvenne which is designed in Switzerland and offers superior qualities.</p>
      <p>To provide you with the best treatment outcome, we perform a full assessment of your facial shape, proportion and muscle activity. For that reason, we offer a comprehensive, initial consultation that allows us to get to know you and, at the same time, carefully assess your personal requirements.</p>
      <p class="link white" style="text-align:left">www.veloura.co.nz/Dermal Filler</p>
    </div>
    <div class="tab tab--grey" style="left:12px;top:445px">Plasma (Vampire Facial)</div>
    <div class="abs body-text white" style="left:20px;top:467px;width:240px">
      <p>This treatment uses growth factors from your own blood to thicken and lift your skin. The advantage of plasma is that it is</p>
      <p>Medical Microneedling with Corvelle Glide 4</p>
    </div>
    <div class="bottom-band" style="background:linear-gradient(90deg,#0a4f9e,var(--navy))"></div>
  </div>

  <div class="panel panel--3" style="background:#fff">
    <div class="rule" style="left:0;width:273px;top:40px"></div>
    <div class="tab tab--blue" style="left:10px;top:33px">Chemical Peel</div>
    <div class="abs body-text" style="left:18px;top:56px;width:240px">
      <p>Peels are solutions made of natural acidic components, often derived from plants, that we gently apply to your skin. The benefit can range from a brightening, exfoliating effect for a milder peel to more deeper peels for uneven pigmentation and skin texture. But it is also a good treatment option to improve acne.</p>
      <p class="link" style="text-align:left">www.veloura.co.nz/Chemical Peel</p>
    </div>
    <div class="pill pill--blue" style="top:158px">Skin Conditions</div>
    <div class="abs body-text" style="left:18px;top:190px;width:240px">
      <p>All our treatments work to boost your complexion and skin from within enhancing your appearance and general wellbeing. For a new, fresher and healthier you.</p>
      <p>Sun damage/signs of ageing</p>
      <p>Signs of sun damage are loss of elasticity and volume loss of your skin as well as uneven pigmentation and skin texture. All these components can be improved with the right treatment options. We are here to advise you on this.</p>
    </div>
    <div class="rule" style="left:0;width:273px;top:329px"></div>
    <div class="tab tab--blue" style="left:10px;top:322px">Chemical Peel</div>
    <div class="abs body-text" style="left:18px;top:345px;width:240px">
      <p>Many different treatment options are available for acne and oily skin. As a first step, it is important that you use the right daily skincare. Following that, we offer a range of treatment options including micro needling, peels and a combination of red and blue light. For more severe cases, our doctors can prescribe isotretinoin, a vitamin A tablet that improves acne but has to be carefully monitored by our doctors.</p>
    </div>
    <div class="rule" style="left:0;width:273px;top:445px"></div>
    <div class="tab tab--blue" style="left:10px;top:438px">Uneven Pigmentation/Melsama</div>
    <div class="abs body-text" style="left:18px;top:462px;width:240px">
      <p>It is important to diagnose pigmentation problems correctly as there are different forms of pigmentation that require different treatments. Often thought of as a very difficult condition to treat, it is rare for us to not achieve a marked improvement.</p>
      <p>There are many more skin and ageing concerns that we have not listed here but please check our website www.veloura.co.nz for comprehensive information.</p>
    </div>
    <div class="bottom-band"></div>
  </div>
</section>

</body>
</html>
```